Letterhead Design Project

Initially, we would like to review our letterheads.

Something simple which uses our corporate imagery well and is nicely balanced.

Please note that I will be following up this letter-head with some customised quote templates and similarly customisable collateral in the next few weeks.

Target Market(s)

Enterprise business

Industry/Entity Type

Quote

Requirements
Must have
• The Norbix7 logo
See www.norbix7.com.au

Our tagline "Enterprise Hosting, Messaging and Server Virtualisation"

Our website address

Ideally in our colour pallette, but will consider submissions which look fantastic and necessitate other colours.

```html
<!DOCTYPE html>
<html lang="en">
<head>
<meta charset="utf-8">
<title>Norbix7 Letterhead</title>
<link href="https://fonts.googleapis.com/css2?family=Arimo:wght@400;700&display=swap" rel="stylesheet">
<style>
  :root {
    --backdrop: #dedede;
    --paper: #f7f7f7;
    --ink: #1a1a1a;
    --header-black: #161616;
    --brand-red: #d0343a;
    --light-text: #e6e6e6;
  }
  * { margin: 0; padding: 0; box-sizing: border-box; }
  html, body {
    width: 1200px; height: 800px; overflow: hidden;
    background: var(--backdrop);
    font-family: "Arimo", Arial, sans-serif;
  }
  .letterhead {
    position: absolute; left: 436px; top: 184px;
    width: 308px; height: 433px;
    background: var(--paper);
  }
  .header {
    position: absolute; left: 0; top: 0; width: 100%; height: 66px;
    background: var(--header-black);
  }
  .brand-mark {
    position: absolute; left: 28px; top: 16px;
    width: 25px; height: 25px; background: var(--brand-red);
  }
  .brand-name {
    position: absolute; left: 57px; top: 13px;
    font-size: 28px; font-weight: 700; letter-spacing: -0.8px;
    color: #ffffff; line-height: 1;
  }
  .tagline {
    position: absolute; left: 28px; top: 43px;
    font-size: 6px; color: var(--light-text); white-space: nowrap;
  }
  .contact {
    position: absolute; left: 194px; top: 15px;
    font-size: 5.8px; line-height: 6.4px; color: var(--light-text);
  }
  .contact .company { color: var(--brand-red); font-weight: 700; font-size: 7px; line-height: 8px; }
  .contact .label { color: var(--brand-red); font-weight: 700; }
  .contact .gap { height: 6px; }
  .rule { position: absolute; height: 5px; }
  .rule.top { top: 66px; }
  .rule.bottom { top: 423px; height: 10px; }
  .rule.dark { left: 0; width: 190px; background: var(--header-black); }
  .rule.red { left: 193px; width: 115px; background: var(--brand-red); }
  .body-copy {
    position: absolute; left: 27px; top: 95px; width: 256px;
    font-size: 5.6px; line-height: 9.3px; color: var(--ink);
  }
  .body-copy .salutation { margin-bottom: 6px; }
  .body-copy p { text-align: justify; margin-bottom: 9.5px; }
  .website {
    position: absolute; left: 43px; top: 413px;
    font-size: 7.5px; letter-spacing: 2.6px; color: var(--ink);
  }
</style>
</head>
<body>
  <div class="letterhead">
    <header class="header">
      <div class="brand-mark"></div>
      <div class="brand-name">Norbix7</div>
      <div class="tagline">Enterprise Hosting, Messaging and Server Virtualisation</div>
      <div class="contact">
        <div class="company">Norbix7 Pty. Ltd.</div>
        <div>Suite 4, Level 3 18 Harlow Crescent,</div>
        <div>Dunmore Vale, Australia VIC - 3920</div>
        <div class="gap"></div>
        <div><span class="label">NSW:</span> +61 2 5550 0192</div>
        <div><span class="label">Email:</span> sales@norbix7.com.au</div>
      </div>
    </header>
    <div class="rule top dark"></div>
    <div class="rule top red"></div>

    <main class="body-copy">
      <div class="salutation">Dear Client,</div>
      <p>Lorem ipsum dolor sit amet, consectetur adipisicing elit, sed do eiusmod tempor incididunt ut labore et dolore magna aliqua. Ut enim ad minim veniam, quis nostrud exercitation ullamco laboris nisi ut aliquip ex ea commodo consequat. Duis aute irure dolor in reprehenderit in voluptate velit esse cillum dolore eu fugiat nulla pariatur. Excepteur sint occaecat cupidatat non proident, sunt in culpa qui officia deserunt mollit anim id est laborum.</p>
      <p>Lorem ipsum dolor sit amet, consectetur adipisicing elit, sed do eiusmod tempor incididunt ut labore et dolore magna aliqua. Ut enim ad minim veniam, quis nostrud exercitation ullamco laboris nisi ut aliquip ex ea commodo consequat. Duis aute irure dolor in reprehenderit in voluptate velit esse cillum dolore eu fugiat nulla pariatur. Excepteur sint occaecat cupidatat non proident, sunt in culpa qui officia deserunt mollit anim id est laborum.</p>
      <p>Lorem ipsum dolor sit amet, consectetur adipisicing elit, sed do eiusmod tempor incididunt ut labore et dolore magna aliqua. Ut enim ad minim veniam, quis nostrud exercitation ullamco laboris nisi ut aliquip ex ea commodo consequat. Duis aute irure dolor in reprehenderit in voluptate velit esse cillum dolore eu fugiat nulla pariatur. Excepteur sint occaecat cupidatat non proident, sunt in culpa qui officia deserunt mollit anim id est laborum.</p>
      <p>Lorem ipsum dolor sit amet, consectetur adipisicing elit, sed do eiusmod tempor incididunt ut labore et dolore magna aliqua. Ut enim ad minim veniam, quis nostrud exercitation ullamco laboris nisi ut aliquip ex ea commodo consequat. Duis aute irure dolor in reprehenderit in voluptate velit esse cillum dolore eu fugiat nulla pariatur. Excepteur sint occaecat cupidatat non proident, sunt in culpa qui officia deserunt mollit anim id est laborum.</p>
      <p>Lorem ipsum dolor sit amet, consectetur adipisicing elit, sed do eiusmod tempor incididunt ut labore et dolore magna aliqua. Ut enim ad minim veniam, quis nostrud exercitation ullamco laboris nisi ut aliquip ex ea commodo consequat. Duis aute irure dolor in reprehenderit in voluptate velit esse cillum dolore eu fugiat nulla pariatur. Excepteur sint occaecat cupidatat non proident, sunt in culpa qui officia deserunt mollit anim id est laborum.</p>
    </main>

    <div class="website">www.norbix7.com.au</div>
    <div class="rule bottom dark"></div>
    <div class="rule bottom red"></div>
  </div>
</body>
</html>
```